Post Card Design - For Financial

"9" length 6.5" height" post card of tallhedge.net trying to get people to text the word YES to our phone number to access our latest stock picks. or marketrove.io we own both of them. Call to action. Get winnin stock picks sign up now text the word "YES" to 888-312-4798. must haves: " track record 2023: 477.8%" "#1 stock picking newsletter in the U.S.A." " Disclaimer: The materials and content provided by TallHedge.net, including but not limited to our website, emails, blogs, and text messages (collectively, the "Materials"), are intended for general information purposes only and do not constitute financial, legal, or investment advice. TallHedge.net is engaged in the business of marketing and advertising companies for compensation. The information contained in the Materials is not, and should not be read as, an offer or recommendation to buy or sell any securities. All content is provided for informational and educational purposes only. TallHedge.net and its staff are not licensed investment advisors, brokers, or dealers. Any content provided by us is not intended to solicit or recommend any investment and should not be used as the basis for any investment decisions. We do not provide investment advice, endorse any financial product, or suggest that any particular investment or strategy is suitable for any specific person. TallHedge.net receives compensation from the companies featured in our alerts, emails, and other Materials for marketing and advertising services. The existence of such compensation may influence the content, topics, or posts made in the Materials. Investing in stocks, especially penny stocks, involves a high level of risk and may not be suitable for all investors. The possibility exists that you could sustain a loss of some or all of your initial investment. Therefore, you should not invest money that you cannot afford to lose. The performance figures stated in the Materials, including but not limited to a track record of 477% in 2023, are hypothetical and should not be considered indicative of future results. Past performance is not necessarily indicative of future results. Individual results may vary, and the examples used in the Materials are not guaranteed to occur. You are encouraged to perform your own due diligence and consult with a qualified financial advisor before making any investment decisions. TallHedge.net and its Materials should not be used as the sole basis for any investment decision. We make no representation or warranty as to the accuracy, completeness, or reliability of the information contained in the Materials. The content provided by TallHedge.net and in its newsletter is intended for entertainment purposes only. Acknowledgment: By using TallHedge.net's services, joining our site, or subscribing to our email/blog list, you acknowledge that you have read, understood, and agree to be bound by the terms of this disclaimer. If you do not agree with these terms, you should not use our services or subscribe to our Materials

."

Target Market(s)

investors

Industry/Entity Type

financial

Colors
0054AA
0677BA
7BADD7
CADEEF
E8F1F8
00AB8E
00BBA5
67D7C9
C6EFE9
E9F9F6
59FF00
82FF00
B8FF75
E3FFCB
F4FFEA

Requirements
Must have
• " track record 2023: 477.8%" "#1 stock picking newsletter in the U.S.A." "Disclaimer: The materials and content provided by TallHedge.net, including but not limited to our website, emails, blogs, and text messages (collectively, the "Materials"), are intended for general information purposes only and do not constitute financial, legal, or investment advice. TallHedge.net is engaged in the business of marketing and advertising companies for compensation. The information contained in the Materials is not, and should not be read as, an offer or recommendation to buy or sell any securities. All content is provided for informational and educational purposes only. TallHedge.net and its staff are not licensed investment advisors, brokers, or dealers. Any content provided by us is not intended to solicit or recommend any investment and should not be used as the basis for any investment decisions. We do not provide investment advice, endorse any financial product, or suggest that any particular investment or strategy is suitable for any specific person. TallHedge.net receives compensation from the companies featured in our alerts, emails, and other Materials for marketing and advertising services. The existence of such compensation may influence the content, topics, or posts made in the Materials. Investing in stocks, especially penny stocks, involves a high level of risk and may not be suitable for all investors. The possibility exists that you could sustain a loss of some or all of your initial investment. Therefore, you should not invest money that you cannot afford to lose. The performance figures stated in the Materials, including but not limited to a track record of 477% in 2023, are hypothetical and should not be considered indicative of future results. Past performance is not necessarily indicative of future results. Individual results may vary, and the examples used in the Materials are not guaranteed to occur. You are encouraged to perform your own due diligence and consult with a qualified financial advisor before making any investment decisions. TallHedge.net and its Materials should not be used as the sole basis for any investment decision. We make no representation or warranty as to the accuracy, completeness, or reliability of the information contained in the Materials. The content provided by TallHedge.net and in its newsletter is intended for entertainment purposes only. Acknowledgment: By using TallHedge.net's services, joining our site, or subscribing to our email/blog list, you acknowledge that you have read, understood, and agree to be bound by the terms of this disclaimer. If you do not agree with these terms, you should not use our services or subscribe to our Materials."
Nice to have
• call to action: Get exclusive stock picks delivered directly to your phone. Text "YES" to [888-312-4798] to receive your first stock pick

```html
<!DOCTYPE html>
<html lang="en">
<head>
<meta charset="UTF-8">
<title>TallHedge Postcard</title>
<link href="https://fonts.googleapis.com/css2?family=Roboto:wght@300;400;500;700;900&display=swap" rel="stylesheet">
<style>
  :root {
    --page-bg: #ececec;
    --card-white: #ffffff;
    --panel-dark: #101820;
    --panel-mid: #1b2a33;
    --accent-green: #8cc63f;
    --text-light: #f2f4f5;
    --bar-blue: #1a7bc4;
    --brand-navy: #0054AA;
    --brand-blue: #0677BA;
    --brand-teal: #00AB8E;
    --tint-blue: #E8F1F8;
    --rule-blue: #CADEEF;
    --ink: #1b2a33;
    --ink-soft: #4a5963;
  }
  html, body {
    margin: 0;
    width: 1200px;
    height: 900px;
    overflow: hidden;
    background: var(--page-bg);
    font-family: 'Roboto', Arial, sans-serif;
  }
  .postcard {
    position: absolute;
    left: 40px;
    top: 50px;
    width: 1120px;
    height: 800px;
    background: var(--card-white);
  }
  .front-panel {
    position: absolute;
    left: 0;
    top: 0;
    width: 552px;
    height: 800px;
    overflow: hidden;
    background: var(--panel-dark);
  }
  .market-backdrop {
    position: absolute;
    inset: 0;
    background:
      radial-gradient(ellipse at 75% 45%, rgba(120, 70, 40, 0.45), transparent 55%),
      radial-gradient(ellipse at 60% 80%, rgba(40, 90, 80, 0.35), transparent 60%),
      linear-gradient(160deg, var(--panel-mid), var(--panel-dark) 70%);
  }
  .accent-bar {
    position: absolute;
    left: 552px;
    top: 60px;
    width: 25px;
    height: 676px;
    background: var(--bar-blue);
  }
  .copy {
    position: absolute;
    left: 76px;
    color: var(--text-light);
    margin: 0;
    white-space: nowrap;
  }
  .headline {
    top: 35px;
    font-size: 47px;
    font-weight: 700;
    line-height: 40px;
    color: var(--accent-green);
    letter-spacing: -0.3px;
  }
  .subtitle {
    top: 182px;
    left: 79px;
    font-size: 23px;
    font-weight: 300;
    line-height: 24px;
  }
  .subtitle em {
    color: var(--accent-green);
    font-weight: 700;
  }
  .subhead {
    top: 270px;
    font-size: 27px;
    font-weight: 700;
    line-height: 34px;
    color: var(--accent-green);
  }
  .body-text {
    top: 358px;
    left: 78px;
    font-size: 16.5px;
    line-height: 18.6px;
  }
  .body-line { font-size: 16.5px; line-height: 19px; }
  .expect { top: 451px; }
  .follow { top: 489px; }
  .benefits {
    top: 526px;
    list-style: none;
    padding: 0;
    font-size: 16.5px;
    line-height: 19px;
  }
  .benefits li {
    position: relative;
    padding-left: 30px;
  }
  .benefits li::before {
    content: "•";
    position: absolute;
    left: 0;
  }
  .pricing {
    top: 638px;
    font-size: 16.5px;
    line-height: 19px;
  }
  .site-url {
    top: 724px;
    left: 89px;
    font-size: 28px;
    color: var(--accent-green);
  }

  /* Reverse side */
  .back-panel {
    position: absolute;
    left: 612px;
    top: 60px;
    width: 476px;
    height: 700px;
    color: var(--ink);
  }
  .rank-label {
    margin: 0;
    font-size: 13px;
    font-weight: 700;
    letter-spacing: 1.2px;
    text-transform: uppercase;
    color: var(--brand-teal);
  }
  .track-record {
    margin: 6px 0 0;
    font-size: 34px;
    font-weight: 900;
    line-height: 38px;
    color: var(--brand-navy);
  }
  .track-record span { color: var(--brand-blue); }
  .cta-box {
    margin-top: 18px;
    padding: 18px 20px 18px 22px;
    background: var(--tint-blue);
    border-left: 6px solid var(--brand-blue);
  }
  .cta-title {
    margin: 0;
    font-size: 20px;
    font-weight: 700;
    color: var(--brand-navy);
  }
  .cta-lead {
    margin: 6px 0 12px;
    font-size: 14px;
    line-height: 18px;
    color: var(--ink-soft);
  }
  .cta-line {
    display: flex;
    align-items: center;
    gap: 12px;
  }
  .phone-icon { flex: none; }
  .cta-text {
    margin: 0;
    font-size: 17px;
    font-weight: 500;
    line-height: 22px;
  }
  .cta-number {
    display: block;
    font-size: 32px;
    font-weight: 900;
    line-height: 36px;
    color: var(--brand-navy);
  }
  .cta-keyword { color: var(--brand-teal); font-weight: 900; }
  .cta-note {
    margin: 10px 0 0;
    font-size: 14px;
    color: var(--ink-soft);
  }
  .disclaimer {
    margin: 20px 0 0;
    padding-top: 10px;
    border-top: 1px solid var(--rule-blue);
    font-size: 7.6px;
    line-height: 9.6px;
    color: var(--ink-soft);
    text-align: justify;
  }
  .disclaimer strong { color: var(--ink); }
  .site-pair {
    margin: 12px 0 0;
    font-size: 14px;
    font-weight: 700;
    color: var(--brand-blue);
  }
</style>
</head>
<body>
  <div class="postcard">
    <div class="front-panel">
      <div class="market-backdrop" role="img" aria-label="Dark stock market candlestick chart with a hand pointing at rising price data"></div>
      <h1 class="copy headline">Get Winning<br>Stock Picks Sent<br>To Your Phone!</h1>
      <p class="copy subtitle">Our picks have <em>BIG</em> potential to<br>increase <em>312%</em> in a couple of days.</p>
      <h2 class="copy subhead">Make money following<br>our stock picks</h2>
      <p class="copy body-text">We do the hard part for you which is finding underval-<br>ued stocks with big potential. All you have to do is<br>receive our stock picks and then see your money<br>increase.</p>
      <p class="copy body-line expect">This next stock pick is expected to have great results!</p>
      <p class="copy body-line follow">Make money following our picks</p>
      <ul class="copy benefits">
        <li>Trusted stock picks</li>
        <li>Trusted research team.</li>
        <li>Proven results</li>
        <li>Make fantastic money.</li>
        <li>We only pick brand new stocks</li>
      </ul>
      <p class="copy pricing">Average alert price: $2.46<br>Projected target: $12.17+</p>
      <p class="copy site-url">marketrove.io</p>
    </div>
    <div class="accent-bar"></div>

    <div class="back-panel">
      <p class="rank-label">#1 stock picking newsletter in the U.S.A.</p>
      <p class="track-record">Track record 2023: <span>477.8%</span></p>

      <div class="cta-box">
        <p class="cta-title">Get winning stock picks. Sign up now!</p>
        <p class="cta-lead">Get exclusive stock picks delivered directly to your phone.</p>
        <div class="cta-line">
          <svg class="phone-icon" width="40" height="40" viewBox="0 0 24 24" aria-hidden="true">
            <circle cx="12" cy="12" r="12" fill="#0677BA"/>
            <path d="M9.2 6.5c.4 0 .7.2.8.6l.7 1.9c.1.3 0 .7-.2.9l-1 .9c.6 1.3 1.6 2.3 2.9 2.9l.9-1c.2-.2.6-.3.9-.2l1.9.7c.4.1.6.4.6.8v1.8c0 .5-.4.9-.9.9C10.6 17.6 6.4 13.4 6.4 8.3c0-.5.4-.9.9-.9h1.9z" fill="#ffffff" transform="translate(0.2 -0.4)"/>
          </svg>
          <p class="cta-text">Text <span class="cta-keyword">"YES"</span> to
            <span class="cta-number">888-312-4798</span></p>
        </div>
        <p class="cta-note">to receive your first stock pick.</p>
      </div>

      <p class="disclaimer"><strong>Disclaimer:</strong> The materials and content provided by TallHedge.net, including but not limited to our website, emails, blogs, and text messages (collectively, the "Materials"), are intended for general information purposes only and do not constitute financial, legal, or investment advice. TallHedge.net is engaged in the business of marketing and advertising companies for compensation. The information contained in the Materials is not, and should not be read as, an offer or recommendation to buy or sell any securities. All content is provided for informational and educational purposes only. TallHedge.net and its staff are not licensed investment advisors, brokers, or dealers. Any content provided by us is not intended to solicit or recommend any investment and should not be used as the basis for any investment decisions. We do not provide investment advice, endorse any financial product, or suggest that any particular investment or strategy is suitable for any specific person. TallHedge.net receives compensation from the companies featured in our alerts, emails, and other Materials for marketing and advertising services. The existence of such compensation may influence the content, topics, or posts made in the Materials. Investing in stocks, especially penny stocks, involves a high level of risk and may not be suitable for all investors. The possibility exists that you could sustain a loss of some or all of your initial investment. Therefore, you should not invest money that you cannot afford to lose. The performance figures stated in the Materials, including but not limited to a track record of 477% in 2023, are hypothetical and should not be considered indicative of future results. Past performance is not necessarily indicative of future results. Individual results may vary, and the examples used in the Materials are not guaranteed to occur. You are encouraged to perform your own due diligence and consult with a qualified financial advisor before making any investment decisions. TallHedge.net and its Materials should not be used as the sole basis for any investment decision. We make no representation or warranty as to the accuracy, completeness, or reliability of the information contained in the Materials. The content provided by TallHedge.net and in its newsletter is intended for entertainment purposes only. <strong>Acknowledgment:</strong> By using TallHedge.net's services, joining our site, or subscribing to our email/blog list, you acknowledge that you have read, understood, and agree to be bound by the terms of this disclaimer. If you do not agree with these terms, you should not use our services or subscribe to our Materials.</p>

      <p class="site-pair">tallhedge.net &nbsp;|&nbsp; marketrove.io</p>
    </div>
  </div>
</body>
</html>
```